Web Design

We need a website for a company based in Doha Qatar called
Velmora Tidy Service.

It is the number one maid cleaning service company, and we have branches all over qatar.

Luxury Cleaning Service Provider.

The color scheme is gold, yellow and black like the logo.

Before they get to the website, there is an intro video.

The website should depict luxury.

Target Market(s)

People who need maids at their houses.

Industry/Entity Type

Cleaning Service

Requirements
Must have
• Luxury, Sleek, Modern

The opening sequence is a video which I already have. Its too big to upload here so I am going to put it on youtube.

After the opening sequence, the home page should have a widescreen photo background and it should change every five seconds, the first background photo should be of qatar westbay skyline. Then the second background should be of maid photos in cleaning positions. Then the third background should be of cleaner photos etc.

We will send you all the tabs and all the content later.

```html
<!DOCTYPE html>
<html lang="en">
<head>
<meta charset="utf-8">
<title>Velmora Tidy Service — Luxury Cleaning Service Provider</title>
<link href="https://fonts.googleapis.com/css2?family=Libre+Baskerville:wght@400;700&family=Roboto:wght@300;400&display=swap" rel="stylesheet">
<style>
  :root {
    --ink-dark: #222426;
    --ink-dark-2: #2e3134;
    --gold: #c9a04a;
    --gold-bright: #d9ab2f;
    --gold-frame: #c8a660;
    --brown: #5b3514;
    --white: #ffffff;
    --text-soft: #4a4f55;
    --nav-grey: #3a3a3a;
    --rule: rgba(255,255,255,0.12);
  }
  * { margin: 0; padding: 0; box-sizing: border-box; }
  html, body { width: 1200px; height: 850px; overflow: hidden; background: var(--white); }
  body { position: relative; font-family: "Roboto", Arial, sans-serif; }

  .topbar {
    position: absolute; left: 0; top: 0; width: 1200px; height: 127px;
    background: linear-gradient(180deg, var(--ink-dark-2), var(--ink-dark));
  }
  .service-nav {
    position: absolute; top: 42px; height: 44px;
    border-top: 1px solid var(--rule); border-bottom: 1px solid var(--rule);
    display: flex; align-items: center; justify-content: space-between;
    font-family: "Libre Baskerville", Georgia, serif; font-size: 15.5px; color: var(--white);
  }
  .service-nav a { color: inherit; text-decoration: none; }
  .service-nav--left { left: 27px; width: 430px; }
  .service-nav--right { left: 737px; width: 428px; }
  .service-nav .is-active { color: var(--gold-bright); }

  .brand {
    position: absolute; left: 487px; top: 0; width: 217px; height: 137px;
    background: var(--white); border: 5px solid var(--gold-frame); border-top: none;
    box-shadow: 0 3px 6px rgba(0,0,0,0.25);
    display: flex; flex-direction: column; align-items: center; justify-content: center; gap: 10px;
    z-index: 3;
  }
  .brand-mark { width: 14px; height: 14px; border-radius: 50%; background: var(--gold); }
  .brand-name {
    font-family: "Libre Baskerville", Georgia, serif; font-size: 17px; color: var(--brown);
    text-align: center; line-height: 1.3;
  }

  .page-nav {
    position: absolute; left: 0; top: 127px; width: 1200px; height: 40px;
    background: var(--white); box-shadow: 0 2px 4px rgba(0,0,0,0.12); z-index: 2;
    font-size: 13px; color: var(--nav-grey);
  }
  .page-nav a { position: absolute; top: 13px; color: inherit; text-decoration: none; }
  .page-nav .is-active { color: var(--gold-bright); }
  .page-nav-pointer { position: absolute; left: 594px; top: 167px; z-index: 2; }

  .hero {
    position: absolute; left: 0; top: 167px; width: 1200px; height: 655px;
    background: linear-gradient(180deg, #4f7ed6 0%, #7fa3e0 30%, #b5c9e6 55%, #cfd6d6 68%, #7e9a8a 76%, #3d7c86 82%, #2b666c 100%);
  }
  .hero-panel {
    position: absolute; left: 140px; top: 320px; width: 911px; height: 329px;
    background: linear-gradient(135deg, #c7a55f, #dcc089 50%, #c29a4f);
    padding: 11px 10px 10px 10px;
  }
  .hero-card {
    width: 100%; height: 100%; background: var(--white);
    text-align: center; padding-top: 42px;
  }
  .hero-kicker { font-weight: 300; font-size: 28px; color: var(--brown); letter-spacing: 0.3px; }
  .hero-title {
    font-family: "Libre Baskerville", Georgia, serif; font-weight: 400;
    font-size: 43px; color: var(--gold); margin-top: 4px;
  }
  .hero-rule { width: 819px; height: 1px; background: var(--gold); margin: 18px auto 0; }
  .hero-text {
    width: 680px; margin: 32px auto 0; font-weight: 300; font-size: 17px; line-height: 25px;
    color: var(--text-soft);
  }
  .slider-dots { position: absolute; left: 547px; top: 790px; display: flex; gap: 6px; }
  .slider-dot { width: 15px; height: 15px; border-radius: 50%; border: 2px solid var(--white); }
  .slider-dot.is-active { border-color: var(--gold-bright); display: flex; align-items: center; justify-content: center; }
  .slider-dot.is-active::after { content: ""; width: 5px; height: 5px; border-radius: 50%; background: var(--gold-bright); }
</style>
</head>
<body>
  <header class="topbar">
    <nav class="service-nav service-nav--left">
      <a href="#">Home Cleaning</a><a href="#">Deep Cleaning</a><a href="#">Vacancy Cleaning</a>
    </nav>
    <nav class="service-nav service-nav--right">
      <a href="#" class="is-active">Home Cleaning</a><a href="#">Deep Cleaning</a><a href="#">Vacancy Cleaning</a>
    </nav>
  </header>

  <div class="brand">
    <span class="brand-mark"></span>
    <span class="brand-name">Velmora Tidy<br>Service</span>
  </div>

  <nav class="page-nav">
    <a href="#" class="is-active" style="left:222px">Home</a>
    <a href="#" style="left:289px">About Us</a>
    <a href="#" style="left:375px">Our Services</a>
    <a href="#" style="left:737px">How It Works</a>
    <a href="#" style="left:848px">Clients</a>
    <a href="#" style="left:921px">Contact Us</a>
  </nav>
  <svg class="page-nav-pointer" width="12" height="7" viewBox="0 0 12 7"><path d="M0 0 L12 0 L6 7 Z" fill="#ffffff"/></svg>

  <section class="hero" role="img" aria-label="Widescreen photo of the Doha West Bay skyline across the water"></section>

  <div class="hero-panel">
    <div class="hero-card">
      <p class="hero-kicker">WE ARE NUMBER ONE</p>
      <h1 class="hero-title">Luxury Cleaning Service Provider</h1>
      <div class="hero-rule"></div>
      <p class="hero-text">Lorem ipsum dolor sit amet, consectetur adipiscing elit. Proin sit amet elit tempus, lobortis nunc eu, suscipit neque. In at urna est. Aliquam erat volutpat. Donec vitae lectus elementum, placerat risus a, euismod arcu.</p>
    </div>
  </div>

  <div class="slider-dots">
    <span class="slider-dot is-active"></span><span class="slider-dot"></span><span class="slider-dot"></span><span class="slider-dot"></span><span class="slider-dot"></span>
  </div>
</body>
</html>
```